Business Card Design for Concierge business

Hi. I would like to have an elegant, smart business card for my concierge business, called Harbor Concierge. The services I provide are mail management, dog walking, cleaning, car, stylist, personal shopper, running errands, property management, event planning. I was thinking to add my picture but I would like to see options without it as well, if possible.

Thank you.

Business Card Details:
*Designers are to solely use contact information for the business card design. This is not to be used to contact the customer*

Name: Mirela Dobos
mail: tidewayconcierge@mailvista.example
Phone: 555-284-1097

Target Market(s)

vacation home owners

Industry/Entity Type

Business

Font styles to use
Serif

Colors

Designer to choose colors to be used in the design.

Requirements
Nice to have
• Could use icons that describe the services I provide for example car, house, key, shopping cart, shopping bags, envelope, champagne glasses, phone, dog etc.

```html
<!DOCTYPE html>
<html lang="en">
<head>
<meta charset="utf-8">
<title>Mirela Dobos – Harbor Concierge Business Card</title>
<link rel="stylesheet" href="https://fonts.googleapis.com/css2?family=Lora:wght@400;700&display=swap">
<style>
  :root {
    --sky: #6f9fd0;
    --sky-light: #c9dcec;
    --sea: #3fb7c4;
    --sea-deep: #1e8fa0;
    --sand: #ece6dc;
    --palm: #6c8a2e;
    --white: #ffffff;
    --ink: #333333;
    --mobile-blue: #3d8fd6;
    --desk-orange: #e9862b;
    --web-green: #56a83c;
    --chat-blue: #3b5a98;
    --loop-blue: #2f9fe0;
    --portrait-tone: #a98a66;
    --service: #1e8fa0;
  }
  * { margin: 0; padding: 0; box-sizing: border-box; }
  html, body { width: 1000px; height: 1200px; overflow: hidden; background: var(--white); }
  body { font-family: "Lora", Georgia, serif; color: var(--ink); }
  .canvas { position: relative; width: 1000px; height: 1200px; }

  .card { position: absolute; left: 0; width: 1000px; height: 600px; overflow: hidden; }
  .card--front { top: 0; background: var(--white); }
  .card--back { top: 600px; }

  .beach-scene {
    position: absolute; left: 0; width: 100%;
    background: linear-gradient(180deg, var(--palm) 0%, var(--sky) 18%, var(--sky-light) 42%, var(--sea) 55%, var(--sea-deep) 62%, var(--sand) 74%, var(--sand) 100%);
  }
  .card--front .beach-scene { top: 0; height: 311px; }
  .card--back .beach-scene { top: 0; height: 600px; }

  .portrait {
    position: absolute; left: 67px; top: 222px; width: 200px; height: 203px;
    background: var(--white); padding: 9px;
    box-shadow: 0 2px 6px rgba(0,0,0,0.35);
  }
  .portrait__photo { width: 100%; height: 100%; background: linear-gradient(160deg, #c7ab84, var(--portrait-tone) 60%, #4a3f38); }

  .identity { position: absolute; color: var(--white); text-shadow: 0 1px 4px rgba(0,0,0,0.55); }
  .identity__name { font-weight: 700; line-height: 1; }
  .identity__title { font-weight: 700; line-height: 1.1; }
  .card--front .identity { left: 294px; top: 236px; }
  .card--front .identity__name { font-size: 34px; }
  .card--front .identity__title { font-size: 19px; margin-top: 4px; }
  .card--back .identity { left: 0; width: 100%; top: 248px; text-align: center; }
  .card--back .identity__name { font-size: 54px; }
  .card--back .identity__title { font-size: 28px; margin-top: 6px; }

  .contact { position: absolute; display: flex; align-items: center; font-size: 21px; color: var(--ink); }
  .contact svg { width: 30px; height: 30px; flex: none; }
  .contact--mobile { left: 308px; top: 347px; }
  .contact--desk { left: 308px; top: 418px; }
  .contact--email { left: 308px; top: 489px; }
  .contact__text { margin-left: 25px; }

  .social { position: absolute; left: 668px; display: flex; align-items: center; font-size: 19px; color: var(--ink); }
  .social--chatterly { top: 342px; }
  .social--loopline { top: 393px; }
  .social__mark { width: 26px; height: 26px; border-radius: 4px; flex: none; }
  .social--chatterly .social__mark { background: var(--chat-blue); }
  .social--loopline .social__mark { background: var(--loop-blue); }
  .social__network { margin-left: 12px; font-weight: 700; color: var(--chat-blue); }
  .social--loopline .social__network { color: var(--loop-blue); }
  .social__handle { margin-left: 8px; }

  .services { position: absolute; left: 0; top: 548px; width: 100%; display: flex; justify-content: center; gap: 44px; }
  .services svg { width: 30px; height: 30px; }
  .services g { fill: none; stroke: var(--service); stroke-width: 2; stroke-linejoin: round; stroke-linecap: round; }
</style>
</head>
<body>
<main class="canvas">
  <section class="card card--front">
    <div class="beach-scene" role="img" aria-label="Tropical beach photo with thatched parasols, palm fronds, turquoise sea and lounge chairs"></div>
    <div class="portrait">
      <div class="portrait__photo" role="img" aria-label="Portrait photo of the concierge owner"></div>
    </div>
    <div class="identity">
      <h1 class="identity__name">Mirela Dobos</h1>
      <p class="identity__title">Harbor Concierge Owner</p>
    </div>

    <div class="contact contact--mobile">
      <svg viewBox="0 0 30 30" aria-hidden="true"><rect x="9" y="3" width="12" height="24" rx="2" fill="var(--mobile-blue)"/><rect x="11" y="6" width="8" height="16" fill="var(--white)"/><circle cx="15" cy="24.5" r="1.2" fill="var(--white)"/></svg>
      <span class="contact__text">555-284-1097</span>
    </div>
    <div class="contact contact--desk">
      <svg viewBox="0 0 30 30" aria-hidden="true"><rect x="5" y="9" width="20" height="18" rx="2" fill="var(--desk-orange)"/><rect x="3" y="3" width="7" height="24" rx="2" fill="var(--desk-orange)"/><g fill="var(--white)"><rect x="13" y="12" width="9" height="3"/><rect x="13" y="18" width="2" height="2"/><rect x="17" y="18" width="2" height="2"/><rect x="21" y="18" width="2" height="2"/><rect x="13" y="22" width="2" height="2"/><rect x="17" y="22" width="2" height="2"/><rect x="21" y="22" width="2" height="2"/></g></svg>
      <span class="contact__text">555-284-1097</span>
    </div>
    <div class="contact contact--email">
      <svg viewBox="0 0 30 30" aria-hidden="true"><g fill="none" stroke="var(--web-green)" stroke-width="2"><circle cx="15" cy="15" r="12"/><ellipse cx="15" cy="15" rx="5" ry="12"/><line x1="3" y1="15" x2="27" y2="15"/><path d="M5 9h20M5 21h20"/></g></svg>
      <span class="contact__text">tidewayconcierge@mailvista.example</span>
    </div>

    <div class="social social--chatterly">
      <span class="social__mark" aria-hidden="true"></span>
      <span class="social__network">Chatterly</span>
      <span class="social__handle">@MirelaDobos</span>
    </div>
    <div class="social social--loopline">
      <span class="social__mark" aria-hidden="true"></span>
      <span class="social__network">Loopline</span>
      <span class="social__handle">@MirelaDobos</span>
    </div>

    <div class="services" aria-label="Services: mail, property, keys, car, shopping, events">
      <svg viewBox="0 0 30 30" aria-hidden="true"><g><rect x="3" y="7" width="24" height="16" rx="1"/><path d="M3 8l12 9 12-9"/></g></svg>
      <svg viewBox="0 0 30 30" aria-hidden="true"><g><path d="M3 15L15 4l12 11"/><path d="M7 12v14h16V12"/><rect x="13" y="18" width="4" height="8"/></g></svg>
      <svg viewBox="0 0 30 30" aria-hidden="true"><g><circle cx="9" cy="15" r="5"/><path d="M14 15h13M23 15v4M19 15v3"/></g></svg>
      <svg viewBox="0 0 30 30" aria-hidden="true"><g><path d="M3 20v-5l3-6h18l3 6v5z"/><path d="M3 15h24"/><circle cx="8.5" cy="21" r="2.5"/><circle cx="21.5" cy="21" r="2.5"/></g></svg>
      <svg viewBox="0 0 30 30" aria-hidden="true"><g><path d="M2 5h4l3 14h15l3-10H8"/><circle cx="11" cy="24" r="2"/><circle cx="22" cy="24" r="2"/></g></svg>
      <svg viewBox="0 0 30 30" aria-hidden="true"><g><rect x="6" y="10" width="18" height="17" rx="1"/><path d="M11 13V8a4 4 0 0 1 8 0v5"/></g></svg>
      <svg viewBox="0 0 30 30" aria-hidden="true"><g><path d="M6 4h8l-1 8a3 3 0 0 1-6 0z"/><path d="M10 15v10M7 25h6"/><path d="M16 4h8l-1 8a3 3 0 0 1-6 0z"/><path d="M20 15v10M17 25h6"/></g></svg>
    </div>
  </section>

  <section class="card card--back">
    <div class="beach-scene" role="img" aria-label="Tropical beach photo with palm fronds, thatched parasols, turquoise sea and lounge chairs on white sand"></div>
    <div class="identity">
      <h2 class="identity__name">Mirela Dobos</h2>
      <p class="identity__title">Harbor Concierge Owner</p>
    </div>
  </section>
</main>
</body>
</html>
```